New homepage design www.quillharbor.nl

We need a new website design to go with our new designed logo.
We are a relativly small basketballclub that would like a shiny new webdesign for our homepage. We want te be able to create a real homepage/base for our clubmembers, where they can find news, upcoming events (agenda/calendar) and the related info on playing basketball at our club (games/tasks/teams and all).

The current website is located at: www.quillharbor.nl but is an outdated and not so appealing design.
There are no real designfeatures of the current site that have to be transferred to the new site.
Coding in HTML/CSS/JS/JPEG/PNG is enough, making a dynamic website will be my task. I just need the design in HTML (preferrably HTML 5)

There is not a huge budget, we are a club without a main sponsor.

Feel free to be creative and amaze us!

Text for the page in the new design will be created by us, you may use some sample text for filling.

Currently used pictures in the site don't have to be transferred to the new page (preferrably not!)
Updates

Tomorrow we will pick a design.

Industry/Entity Type

Events

Requirements
Must have
• The new logo as uploaded and attached.
News page.
Agenda page
HTML compatible same look and feel in all modern browsers (IE, FireFox, Chrome, Safari)
Nice to have
• HTML 5 validated and approved

```html
<!DOCTYPE html>
<html lang="nl">
<head>
<meta charset="utf-8">
<title>Quill Harbor Basketball</title>
<link href="https://fonts.googleapis.com/css2?family=Open+Sans:wght@300;400;600;700&display=swap" rel="stylesheet">
<style>
:root{
  --navy:#162033;
  --navy-2:#22324d;
  --blue:#3b8fdc;
  --blue-dark:#2a6fb5;
  --orange:#ef7a1e;
  --light:#efefef;
  --white:#ffffff;
  --text:#555b63;
  --dark:#2a2a2a;
  --darker:#1e1e1e;
  --foot-text:#b9b9b9;
}
*{box-sizing:border-box;margin:0;padding:0}
html,body{width:744px;height:1200px;overflow:hidden}
body{font-family:"Open Sans",Arial,sans-serif;color:var(--text);background:var(--white);font-size:11px}
.hero{position:relative;height:347px;background:linear-gradient(100deg,var(--navy) 0%,var(--navy-2) 55%,#4a6a92 100%);overflow:hidden}
.hero-art{position:absolute;right:0;top:0;width:380px;height:347px;background:radial-gradient(ellipse at 55% 45%,#7fb6e6 0%,#3a6c9f 45%,rgba(34,50,77,0) 75%)}
.brand{position:absolute;left:34px;top:10px;display:flex;align-items:center;gap:7px}
.brand-dot{width:34px;height:34px;border-radius:50%;background:var(--orange);flex-shrink:0}
.brand-name{font-weight:700;font-size:14px;color:var(--white);letter-spacing:.3px;white-space:nowrap}
.nav{position:absolute;left:212px;top:0;display:flex}
.nav a{display:block;padding:10px 9px 9px;color:var(--white);text-decoration:none;font-size:11px;white-space:nowrap}
.nav a.active{background:var(--orange)}
.hero-title{position:absolute;left:34px;top:108px;font-weight:300;font-size:37px;line-height:43px;color:var(--white)}
.hero-title .accent{color:var(--orange)}
.hero-btn{position:absolute;left:34px;top:285px;width:404px;height:32px;background:var(--orange);color:var(--white);font-size:13px;display:flex;align-items:center;padding-left:12px;gap:10px}
.hero-btn .ico{width:16px;height:16px;border-radius:50%;background:var(--white);display:flex;align-items:center;justify-content:center}
.welcome{position:relative;height:218px;background:var(--light);padding:30px 60px 0 205px}
.welcome-art{position:absolute;left:58px;top:38px;width:110px;height:150px;background:linear-gradient(180deg,#3a3a3a,#111);border-radius:50% 50% 8px 8px / 30% 30% 8px 8px}
.section-title{font-size:22px;font-weight:600;color:var(--dark);margin-bottom:16px}
.welcome p{font-size:10px;line-height:16px}
.features{display:flex;gap:23px;padding:22px 48px 0;height:220px}
.feature{width:140px;height:190px;background:var(--light);position:relative;text-align:center;padding-top:24px}
.feature .num{width:56px;height:56px;border-radius:50%;background:var(--blue);border:4px solid #cfe3f6;color:var(--white);font-size:22px;line-height:48px;margin:0 auto 12px}
.feature h3{font-size:12px;font-weight:600;color:var(--dark);margin-bottom:6px}
.feature p{font-size:8.5px;line-height:12px;padding:0 12px}
.feature .more{position:absolute;right:0;bottom:0;width:20px;height:20px;background:#9a9a9a;display:flex;align-items:center;justify-content:center}
.events{display:flex;height:165px;padding:8px 48px 0}
.events-art{width:300px;height:150px;background:linear-gradient(90deg,#e6e6e6,#9a9a9a 60%,#1a1a1a);border-radius:4px}
.events-list{padding-left:60px;flex:1}
.events-list .section-title{font-size:24px;margin-bottom:10px}
.event{display:flex;gap:12px;margin-bottom:10px}
.date{width:40px;height:44px;background:var(--orange);color:var(--white);text-align:center;font-size:17px;font-weight:700;line-height:22px;flex-shrink:0}
.date small{display:block;font-size:9px;line-height:12px;font-weight:400}
.event h4{color:var(--orange);font-size:10px;font-weight:700;margin-bottom:2px}
.event p{font-size:8.5px;line-height:11px}
.footer{height:218px;background:var(--dark);display:flex;padding:10px 48px 0;gap:40px;color:var(--foot-text)}
.footer h5{color:var(--white);font-size:14px;font-weight:600;margin-bottom:10px}
.col{width:175px}
.links li{list-style:none;font-size:9.5px;line-height:14px}
.links li::before{content:"› ";color:var(--orange)}
.social li{list-style:none;display:flex;align-items:center;gap:8px;font-size:10px;margin-bottom:7px}
.social .sq{width:20px;height:20px;background:var(--blue-dark)}
.contact p{font-size:10px;line-height:15px}
.contact .hl{color:var(--orange)}
.copyright{height:32px;background:var(--darker);color:var(--foot-text);font-size:9.5px;line-height:12px;padding:10px 48px}
.copyright span{color:var(--orange)}
</style>
</head>
<body>
<header class="hero">
  <div class="hero-art" role="img" aria-label="Illustration of a basketball player dunking on a blue paint-splash background"></div>
  <div class="brand"><span class="brand-dot"></span><span class="brand-name">QUILL HARBOR</span></div>
  <nav class="nav">
    <a class="active" href="#">Home</a><a href="#">Teams</a><a href="#">Informatie</a><a href="#">Fotogalerij</a><a href="#">Links</a><a href="#">Gastenboek</a><a href="#">Inloggen</a><a href="#">Contact</a>
  </nav>
  <h1 class="hero-title">Iedereen een gelukkig,<br>gezond en bovenal<br><span class="accent">sportief 2014 gewenst!</span></h1>
  <div class="hero-btn"><span class="ico"><svg width="8" height="8" viewBox="0 0 8 8"><path d="M2 1l4 3-4 3z" fill="#ef7a1e"/></svg></span>International and global basketball news</div>
</header>

<section class="welcome">
  <div class="welcome-art" role="img" aria-label="Silhouette of a basketball player shooting"></div>
  <h2 class="section-title">Welcome To Our Site</h2>
  <p>Welkom bij de basketbalvereniging Quill Harbor, een gezellige club voor jong en oud. Bij ons kun je trainen, wedstrijden spelen en samen plezier maken op en naast het veld. Op deze site vind je het laatste nieuws, de agenda, informatie over teams, trainingstijden en taken. Nieuwe leden zijn altijd welkom om een keer mee te trainen. Heb je vragen over lidmaatschap of de competitie, neem dan gerust contact op met het bestuur. Wij zien je graag in de sporthal!</p>
</section>

<section class="features">
  <div class="feature"><div class="num">01</div><h3>THE TEAMS</h3><p>Bekijk hier alle teams van onze club, met spelers, coaches en uitslagen.</p><span class="more"><svg width="8" height="8" viewBox="0 0 8 8"><path d="M2 1l4 3-4 3z" fill="#fff"/></svg></span></div>
  <div class="feature"><div class="num">02</div><h3>TRAINEN</h3><p>Alle trainingstijden per team en de locaties van de sporthallen op een rij.</p><span class="more"><svg width="8" height="8" viewBox="0 0 8 8"><path d="M2 1l4 3-4 3z" fill="#fff"/></svg></span></div>
  <div class="feature"><div class="num">03</div><h3>EXTERNEN</h3><p>Informatie voor gasten, scheidsrechters en bezoekende teams van buiten.</p><span class="more"><svg width="8" height="8" viewBox="0 0 8 8"><path d="M2 1l4 3-4 3z" fill="#fff"/></svg></span></div>
  <div class="feature"><div class="num">04</div><h3>CLUBSTANDEN</h3><p>De actuele standen van alle teams in hun competitie, elke week bijgewerkt.</p><span class="more"><svg width="8" height="8" viewBox="0 0 8 8"><path d="M2 1l4 3-4 3z" fill="#fff"/></svg></span></div>
</section>

<section class="events">
  <div class="events-art" role="img" aria-label="Illustration of basketball players beside a round black badge"></div>
  <div class="events-list">
    <h2 class="section-title">Upcoming events</h2>
    <div class="event"><div class="date">20<small>FEB</small></div><div><h4>GEEN TRAINING IVM CARNAVAL</h4><p>In verband met carnaval zijn er deze week geen trainingen. Alle teams hervatten de training weer volgens schema.</p></div></div>
    <div class="event"><div class="date">24<small>FEB</small></div><div><h4>GEEN TRAINING IVM CARNAVAL</h4><p>Ook op deze dag vervallen alle trainingen. Wedstrijden in het weekend gaan gewoon door zoals gepland.</p></div></div>
  </div>
</section>

<footer class="footer">
  <div class="col"><h5>Quick Contact</h5>
    <ul class="links"><li>Home</li><li>Teams</li><li>Informatie</li><li>Fotogalerij</li><li>Links</li><li>Gastenboek</li><li>Inloggen</li><li>Contact</li></ul>
  </div>
  <div class="col"><h5>Social Link</h5>
    <ul class="social"><li><span class="sq"></span>Clubwall</li><li><span class="sq"></span>RSS</li><li><span class="sq"></span>Chirper</li><li><span class="sq"></span>Clipcast</li></ul>
  </div>
  <div class="col contact"><h5>Contact Us</h5>
    <p>Sporthal de Haven<br>Havenlaan 12<br>3011 AB Quillhaven<br><span class="hl">Phone: 010 555 0192</span><br><span class="hl">Email: info@quillharbor.nl</span></p>
  </div>
</footer>
<div class="copyright">Copyright © 2014 <span>www.quillharbor.nl</span> All Rights Reserved.</div>
</body>
</html>
```